Velvet Bloom Marisol's Cleaning Service Business Cards Project

A business card with all contact details with logo design on there (already have a logo) eye catching Logo and contact info on one side, full logo on the back, must target upper class residential and corporate companies, fitness companies, still keep it on the feminine side of things , must look elegant

Target Market(s)

Upper class homes and corporate companies

Industry/Entity Type

Cleaning Service

Contact Information for Business Card

Name: Marisol Denhart
Position: Director
ABN: 47193062857
Email: marisolsvelvetcleaning@brightmail.example
Number: 0418926547

Font styles to use
Decorative

Colors

Designer to choose colors to be used in the design.

Requirements
Must have
• Available Sydney Wide, contact info and logo on one side, full logo on the back
Nice to have
• Professional appearance
Should not have
• Cheap advert looking stuff

```html
<!DOCTYPE html>
<html lang="en">
<head>
<meta charset="utf-8">
<title>Velvet Bloom – Business Cards</title>
<link rel="stylesheet" href="https://fonts.googleapis.com/css2?family=Cinzel:wght@600&family=Open+Sans:ital,wght@0,400;0,600;1,600&display=swap">
<style>
  :root {
    --backdrop: #33454d;
    --card: #030303;
    --teal: #5ec4c4;
    --white: #ffffff;
    --ghost: #1b2a2e;
  }
  * { box-sizing: border-box; margin: 0; padding: 0; }
  html, body { width: 1200px; height: 1200px; overflow: hidden; }
  body {
    background: var(--backdrop);
    font-family: "Open Sans", Arial, sans-serif;
    display: flex;
    flex-direction: column;
    align-items: center;
    justify-content: center;
    gap: 50px;
  }
  .card {
    position: relative;
    width: 920px;
    height: 520px;
    background: var(--card);
    overflow: hidden;
  }
  .card__rule {
    position: absolute;
    left: 0; right: 0;
    bottom: 44px;
    height: 5px;
    background: var(--teal);
  }
  .brand {
    position: absolute;
    left: 0; right: 0;
    text-align: center;
  }
  .brand__name {
    font-family: "Cinzel", Georgia, serif;
    font-weight: 600;
    color: var(--teal);
    font-size: 52px;
    letter-spacing: 1px;
    line-height: 1;
  }
  .brand__tagline {
    margin-top: 16px;
    color: var(--white);
    font-size: 15px;
    letter-spacing: 7px;
    text-transform: uppercase;
  }
  .card--back .brand { top: 190px; }
  .card--front .brand { top: 150px; }
  .card__ghost-mark {
    position: absolute;
    left: -70px; top: -20px;
    width: 330px; height: 330px;
    border-radius: 50%;
    background: var(--ghost);
    opacity: .7;
  }
  .contact {
    position: absolute;
    left: 70px;
    bottom: 82px;
    list-style: none;
    display: flex;
    flex-direction: column;
    gap: 6px;
  }
  .contact__item {
    display: flex;
    align-items: center;
    gap: 12px;
    color: var(--white);
    font-style: italic;
    font-weight: 600;
    font-size: 20px;
  }
  .contact__icon { width: 26px; height: 26px; flex: none; }
  .person {
    position: absolute;
    right: 60px;
    bottom: 86px;
    display: flex;
    align-items: center;
    gap: 16px;
  }
  .person__dot {
    width: 44px; height: 44px;
    border-radius: 50%;
    border: 2px solid var(--teal);
  }
  .person__name {
    color: var(--white);
    font-weight: 600;
    font-size: 34px;
    line-height: 1.05;
  }
  .person__role {
    color: var(--teal);
    font-weight: 600;
    font-size: 22px;
    line-height: 1.1;
  }
</style>
</head>
<body>

  <section class="card card--back" aria-label="Card back">
    <div class="brand">
      <div class="brand__name">Velvet Bloom</div>
      <div class="brand__tagline">Marisol’s Cleaning Service</div>
    </div>
    <div class="card__rule"></div>
  </section>

  <section class="card card--front" aria-label="Card front">
    <div class="card__ghost-mark"></div>
    <div class="brand">
      <div class="brand__name">Velvet Bloom</div>
      <div class="brand__tagline">Marisol’s Cleaning Service</div>
    </div>

    <ul class="contact">
      <li class="contact__item">
        <svg class="contact__icon" viewBox="0 0 24 24" aria-hidden="true">
          <rect x="6.5" y="2" width="11" height="20" rx="2" fill="none" stroke="var(--teal)" stroke-width="2"/>
          <line x1="10.5" y1="18.5" x2="13.5" y2="18.5" stroke="var(--teal)" stroke-width="2"/>
        </svg>
        <span>0418926547</span>
      </li>
      <li class="contact__item">
        <svg class="contact__icon" viewBox="0 0 24 24" aria-hidden="true">
          <rect x="2" y="5" width="20" height="14" rx="1" fill="var(--teal)"/>
          <polyline points="2,6 12,13 22,6" fill="none" stroke="var(--card)" stroke-width="1.6"/>
        </svg>
        <span>marisolsvelvetcleaning@brightmail.example</span>
      </li>
      <li class="contact__item">
        <svg class="contact__icon" viewBox="0 0 24 24" aria-hidden="true">
          <path d="M6.6 2.5l3 3.2-1.9 2.6c1.2 2.6 3.3 4.8 6 6l2.6-1.9 3.2 3-2 3.6C11 19.2 4.8 13 4.5 4.6z" fill="var(--teal)"/>
        </svg>
        <span>47193062857</span>
      </li>
    </ul>

    <div class="person">
      <div class="person__dot"></div>
      <div>
        <div class="person__name">Marisol Denhart</div>
        <div class="person__role">Director</div>
      </div>
    </div>

    <div class="card__rule"></div>
  </section>

</body>
</html>
```